Waterproofing specialist needs a flyer design

Our company does repair works for any leakage problems, for example, concrete roofs, balcony, toilets & bathroom, etc. We want our flyers to have a certain focus on the home services that we provide, mainly toilets & bathrooms but not leaving out the rest.

For toilet leakages, we use flood infusion method to water proof and repair toilets. Hence, we like to promote there will be No dust, No noise, No smell, No drilling, No hacking and No removal of existing tile finish. The types of chemical used to manage leakage problems are non-toxic and stops re-bar corrosion. Best of all, it only requires only One-day work. We also provide a call for free consultation.

As we do not have a good picture on waterproofing for illustration, you're welcome to come up with your own pictures that deem fit. The design should communicate reliability and safety.
---------------------------------------------------------

Hi, I have uploaded some of our project pictures for your reference. It is to show an example of what we do in waterproofing. We seal up cracked ceilings or walls basically to prevent water leakage. Understood that the pictures came from RUNFrame, as such, I have also done some research. Searching for "Water damage ceiling" is more relevant our profession. However, I did find more pictures from lenvaultery. I have uploaded one example that can be used. Do feedback to me if the uploads helped or more photos are needed to support your design.

Households

Concrete

• Pictures

```html
<!DOCTYPE html>
<html lang="en">
<head>
<meta charset="utf-8">
<title>Tidewell Waterproofing Flyer</title>
<link href="https://fonts.googleapis.com/css2?family=Open+Sans:wght@700;800&display=swap" rel="stylesheet">
<style>
  :root {
    --frame: #000000;
    --paper: #f5f9e9;
    --brand-blue: #2e74b9;
    --navy: #1c2a8c;
    --white: #ffffff;
    --art-sky: #3f8fd0;
    --art-green: #a4c93a;
  }
  html, body {
    margin: 0;
    padding: 0;
    width: 900px;
    height: 1200px;
    overflow: hidden;
    background: var(--frame);
    font-family: "Open Sans", Verdana, sans-serif;
  }
  .flyer {
    position: absolute;
    left: 42px;
    top: 19px;
    width: 821px;
    height: 1159px;
    background: var(--paper);
    overflow: hidden;
  }
  .shapes {
    position: absolute;
    left: 0;
    top: 0;
  }
  .method-panel {
    position: absolute;
    left: 91px;
    top: 0;
    width: 302px;
    height: 626px;
    color: var(--white);
    text-align: center;
  }
  .method-intro {
    margin: 0;
    padding-top: 68px;
    font-size: 22px;
    line-height: 34px;
    font-weight: 700;
  }
  .wave-icon {
    display: block;
    margin: 0 auto;
  }
  .method-panel .wave-icon { margin-top: 22px; }
  .benefits {
    list-style: none;
    margin: 6px 0 0;
    padding: 0;
    font-size: 25px;
    line-height: 43px;
    font-weight: 700;
  }
  .brand {
    position: absolute;
    left: 428px;
    top: 190px;
    display: flex;
    align-items: center;
    gap: 14px;
    color: var(--navy);
    font-weight: 800;
  }
  .brand-dot {
    width: 72px;
    height: 72px;
    border-radius: 50%;
    background: var(--navy);
    flex: none;
  }
  .brand-name {
    font-size: 32px;
    line-height: 36px;
    letter-spacing: 1px;
  }
  .brand-name span {
    display: block;
    font-size: 19px;
    line-height: 24px;
    letter-spacing: 1px;
  }
  .chemical-panel {
    position: absolute;
    left: 478px;
    top: 522px;
    width: 301px;
    color: var(--white);
    text-align: center;
  }
  .chemical-copy {
    margin: 0;
    font-size: 17.5px;
    line-height: 38.5px;
    font-weight: 700;
    white-space: nowrap;
  }
  .chemical-panel .wave-icon { margin-top: 14px; }
  .contact {
    list-style: none;
    margin: 6px 0 0 -30px;
    width: 361px;
    padding: 0;
    font-size: 31px;
    line-height: 51px;
    font-weight: 700;
  }
  .shelter-art {
    position: absolute;
    left: 19px;
    top: 685px;
    width: 440px;
    height: 350px;
    border-radius: 48% 48% 14px 14px / 34% 34% 14px 14px;
    background: linear-gradient(180deg, var(--art-sky) 0%, var(--art-sky) 28%, var(--art-green) 62%, #7f9e25 100%);
  }
</style>
</head>
<body>
<main class="flyer">
  <svg class="shapes" width="821" height="1159" viewBox="0 0 821 1159" aria-hidden="true">
    <path d="M91 0 H393 V613 Q393 626 380 626 H104 Q91 626 91 613 Z" fill="var(--brand-blue)"/>
    <path d="M478 470 Q478 457 491 457 H766 Q779 457 779 470 V1000 H478 Z" fill="var(--brand-blue)"/>
    <path d="M0 1028 C110 1076 280 1050 420 960 C560 870 650 762 821 768 V1159 H0 Z" fill="var(--brand-blue)"/>
  </svg>

  <section class="method-panel">
    <p class="method-intro">For toilet leakages,<br>we use<br>flood infusion method<br>to water proof<br>and repair toilets.</p>
    <svg class="wave-icon" width="120" height="28" viewBox="0 0 120 28" aria-hidden="true">
      <g fill="none" stroke="var(--white)" stroke-width="2.5">
        <path d="M2 5 q14.5 -6 29 0 t29 0 t29 0 t29 0"/>
        <path d="M2 14 q14.5 -6 29 0 t29 0 t29 0 t29 0"/>
        <path d="M2 23 q14.5 -6 29 0 t29 0 t29 0 t29 0"/>
      </g>
    </svg>
    <ul class="benefits">
      <li>No dust</li>
      <li>No noise</li>
      <li>No smell</li>
      <li>No drilling</li>
      <li>No hacking</li>
      <li>and No removal</li>
      <li>of existing tile finish</li>
    </ul>
  </section>

  <div class="brand">
    <div class="brand-dot"></div>
    <div class="brand-name">TIDEWELL<span>WATERPROOFING</span></div>
  </div>

  <div class="shelter-art" role="img" aria-label="Illustration of a green house sheltered under a large blue patio umbrella"></div>

  <section class="chemical-panel">
    <p class="chemical-copy">The types of chemical<br>used to manage<br>leakage problems<br>are non-toxic<br>and stops re-bar corrosion.<br>Best of all,<br>it only requires<br>only One-day work.<br>We also provide a call<br>for free consultation.</p>
    <svg class="wave-icon" width="96" height="24" viewBox="0 0 96 24" aria-hidden="true">
      <g fill="none" stroke="var(--white)" stroke-width="2.5">
        <path d="M2 4 q11.5 -5 23 0 t23 0 t23 0 t23 0"/>
        <path d="M2 12 q11.5 -5 23 0 t23 0 t23 0 t23 0"/>
        <path d="M2 20 q11.5 -5 23 0 t23 0 t23 0 t23 0"/>
      </g>
    </svg>
    <ul class="contact">
      <li>mobile phone</li>
      <li>email</li>
      <li>company address</li>
    </ul>
  </section>
</main>
</body>
</html>
```